business card for retail pharmacy
Brookfield Pharmacy
Project: business card for retail pharmacy
business card for retail pharmacy - Pharmacy/Pharmaceuticals
Creative Brief
Simple
Gerald P. Ostrander RPh
Owner/Pharmacist
4217 Route 531, Unit #3, Southampton, NJ 08088
brookrxcare7@mailvessel.com
www.brookfieldrxnj-example.com
Hours Monday-Friday 9-7, Saturday 9-1
brookrxcare7 brookrxcare7
Would like to see some cards as red and blue NOT red and gray. We are still not finalized on the logo colors so I would like to see as a red and dark ble combination.
Plidor Plidor

```html
<!DOCTYPE html>
<html lang="en">
<head>
<meta charset="utf-8">
<title>Brookfield Pharmacy – Business Card</title>
<link rel="stylesheet" href="https://fonts.googleapis.com/css2?family=Cinzel:wght@700&family=Open+Sans:wght@400;600&display=swap">
<style>
  :root {
    --backdrop: #232323;
    --card: #ffffff;
    --brand-red: #c41e2a;
    --navy: #1c2d5a;
    --soft-blue: #c8d2e6;
    --text-navy: #3a4766;
  }
  html, body {
    margin: 0;
    padding: 0;
    width: 1200px;
    height: 754px;
    overflow: hidden;
    background: var(--backdrop);
  }
  .canvas {
    position: relative;
    width: 1200px;
    height: 754px;
  }
  .card {
    position: absolute;
    width: 520px;
    height: 296px;
    background: var(--card);
    box-shadow: 0 8px 24px rgba(0,0,0,0.45);
    overflow: hidden;
  }
  .card--front { left: 50px; top: 120px; }
  .card--back  { left: 630px; top: 338px; }

  .brand {
    display: flex;
    align-items: center;
    gap: 10px;
  }
  .brand__dot {
    width: 14px;
    height: 14px;
    border-radius: 50%;
    background: var(--brand-red);
    flex: none;
  }
  .brand__name {
    font-family: "Cinzel", serif;
    font-weight: 700;
    color: var(--brand-red);
    line-height: 1.05;
    text-transform: uppercase;
    letter-spacing: 0.5px;
  }
  .card--front .brand {
    position: absolute;
    left: 0; right: 0; top: 118px;
    justify-content: center;
  }
  .card--front .brand__name { font-size: 26px; }

  .card__waves {
    position: absolute;
    left: 0; top: 0;
    width: 520px;
    height: 296px;
  }
  .card--back .brand {
    position: absolute;
    left: 30px; top: 148px;
  }
  .card--back .brand__name { font-size: 19px; width: 150px; }

  .contact {
    position: absolute;
    left: 290px;
    top: 30px;
    font-family: "Open Sans", sans-serif;
  }
  .contact__name {
    font-weight: 600;
    font-size: 11px;
    letter-spacing: 0.8px;
    color: var(--brand-red);
    text-transform: uppercase;
    margin: 0;
  }
  .contact__role {
    font-size: 8.5px;
    color: var(--navy);
    margin: 2px 0 10px;
  }
  .contact__list {
    list-style: none;
    margin: 0;
    padding: 0;
  }
  .contact__item {
    display: flex;
    align-items: center;
    gap: 8px;
    font-size: 8.5px;
    color: var(--text-navy);
    height: 14px;
  }
  .contact__icon {
    width: 9px;
    height: 9px;
    fill: var(--brand-red);
    flex: none;
  }
  .address {
    position: absolute;
    right: 40px;
    bottom: 30px;
    font-family: "Open Sans", sans-serif;
    font-size: 10px;
    color: #ffffff;
    letter-spacing: 0.3px;
    margin: 0;
  }
</style>
</head>
<body>
<main class="canvas">

  <section class="card card--front" aria-label="Card front">
    <div class="brand">
      <span class="brand__dot"></span>
      <span class="brand__name">Brookfield Pharmacy</span>
    </div>
  </section>

  <section class="card card--back" aria-label="Card back">
    <svg class="card__waves" viewBox="0 0 520 296" aria-hidden="true">
      <path d="M0,188 C150,232 340,172 520,124 L520,130 C340,178 150,238 0,194 Z" fill="var(--soft-blue)"/>
      <path d="M0,197 C150,241 340,181 520,134 L520,152 C340,198 150,258 0,214 Z" fill="var(--navy)"/>
      <path d="M0,218 C150,262 340,202 520,156 L520,296 L0,296 Z" fill="var(--brand-red)"/>
    </svg>

    <div class="brand">
      <span class="brand__dot"></span>
      <span class="brand__name">Brookfield Pharmacy</span>
    </div>

    <div class="contact">
      <p class="contact__name">Gerald P. Ostrander RPh</p>
      <p class="contact__role">Owner/Pharmacist</p>
      <ul class="contact__list">
        <li class="contact__item">
          <svg class="contact__icon" viewBox="0 0 10 10"><path d="M2,0.5 L3.8,0.5 L4.4,3 L3.2,3.8 C3.8,5 4.8,6 6,6.6 L6.8,5.4 L9.4,6 L9.4,7.8 C9.4,8.8 8.6,9.5 7.6,9.4 C4,9 0.9,6 0.5,2.3 C0.4,1.3 1,0.5 2,0.5 Z"/></svg>
          <span>555 014 2201</span>
        </li>
        <li class="contact__item">
          <svg class="contact__icon" viewBox="0 0 10 10"><rect x="2.5" y="0.5" width="5" height="9" rx="1"/></svg>
          <span>555 014 2202</span>
        </li>
        <li class="contact__item">
          <svg class="contact__icon" viewBox="0 0 10 10"><rect x="0.5" y="3" width="9" height="5" rx="1"/><rect x="2.5" y="0.5" width="5" height="3"/></svg>
          <span>555 014 2203</span>
        </li>
        <li class="contact__item">
          <svg class="contact__icon" viewBox="0 0 10 10"><path d="M0.5,2 L9.5,2 L9.5,8 L0.5,8 Z M1,2.4 L5,5.4 L9,2.4" stroke="#fff" stroke-width="0.7"/></svg>
          <span>brookrxcare7@mailvessel.com</span>
        </li>
        <li class="contact__item">
          <svg class="contact__icon" viewBox="0 0 10 10"><circle cx="5" cy="5" r="4.5"/></svg>
          <span>www.brookfieldrxnj-example.com</span>
        </li>
        <li class="contact__item">
          <svg class="contact__icon" viewBox="0 0 10 10"><circle cx="5" cy="5" r="4.5"/><path d="M5,2.2 L5,5 L7,6" stroke="#fff" stroke-width="0.9" fill="none"/></svg>
          <span>Mon–Fri 9–7, Sat 9–1</span>
        </li>
      </ul>
    </div>

    <p class="address">4217 Route 531, Unit #3, Southampton, NJ 08088</p>
  </section>

</main>
</body>
</html>
```